Harbouring Dawn Rituals creates individual, personalised ceremonies to celebrate weddings, naming days,coming of age, significant age, divorce and final resting rites. Ceremonies and meaningful rituals are created in collaboration with the individual to reflect their hopes and desires, how they will/have embrace/d their lives. The final design should have the logo (purple) on a white/silver background on the right hand side of the card. Name of business and contact details in red on a black background on the left
Updates

Hi All, have only just realised I have paid for a double sided card, yep, a newbie! Sorry to set the cat amongst the pigeons but could we put 'creating...... etc' on the back?

Target Market(s)

Couples marrying, renewing of vows, baby naming days, coming of age, significant age, divorce, funeral ceremonies. The target market predominantly will be couples marrying.

Industry/Entity Type

Business

Contact Information for Business Card

Harbouring Dawn Rituals, Doriane Whitcombe, 0428-735902 harbouringdawnrituals1@examplemail.test
"Shaping singular, tailored rituals harbouring dawn"

Font styles to use
Script

Colors
eb1f27
6b449b
f3f0f8

Requirements
Must have
• On initial entry, and now, the logo was not displayed in full - the bottom part was cut off - this needs to be in it's entirety. Colours as previously specified are non-negotiable. Font and placement of characters will be assessed as produced.
Should not have
• Telephone symbol, call us, director,grammatical symbols ( : )

```html
<!DOCTYPE html>
<html lang="en">
<head>
<meta charset="utf-8">
<title>Harbouring Dawn Rituals — Business Card</title>
<link rel="stylesheet" href="https://fonts.googleapis.com/css2?family=Great+Vibes&family=Open+Sans:wght@400;600&display=swap">
<style>
  :root {
    --backdrop: #e4e2e6;
    --card-black: #050505;
    --ink-red: #eb1f27;
    --brand-purple: #6b449b;
    --silver-light: #f3f0f8;
    --silver-mid: #d9d8dc;
    --faint-mark: #1a1a1a;
    --card-w: 540px;
    --card-h: 329px;
  }
  * { box-sizing: border-box; margin: 0; padding: 0; }
  html, body {
    width: 1200px; height: 784px; overflow: hidden;
    background: var(--backdrop);
  }
  .sheet {
    width: 1200px; height: 784px;
    display: flex; align-items: center; justify-content: center; gap: 40px;
  }
  .card {
    position: relative;
    width: var(--card-w); height: var(--card-h);
    overflow: hidden;
    box-shadow: 0 6px 18px rgba(0,0,0,0.18);
  }

  /* Back */
  .card-back { background: var(--card-black); }
  .back-mark {
    position: absolute; left: 0; right: 0; top: 120px;
    text-align: center;
    font-family: "Open Sans", sans-serif; font-weight: 600;
    font-size: 44px; color: var(--faint-mark);
    letter-spacing: 1px;
  }
  .tagline {
    position: absolute; left: 0; right: 0; top: 152px;
    text-align: center;
    font-family: "Open Sans", sans-serif; font-weight: 400;
    font-size: 16px; letter-spacing: 0.6px;
    color: var(--ink-red);
  }

  /* Front */
  .card-front {
    background: linear-gradient(180deg, var(--silver-light) 0%, var(--silver-mid) 60%);
  }
  .front-shapes { position: absolute; inset: 0; width: 100%; height: 100%; }
  .brand-mark {
    position: absolute; top: 30px; right: 30px;
    display: flex; align-items: center; gap: 8px;
    font-family: "Open Sans", sans-serif; font-weight: 600;
    font-size: 15px; color: var(--brand-purple);
  }
  .brand-mark .dot {
    width: 14px; height: 14px; border-radius: 50%;
    background: var(--brand-purple);
  }
  .business-name {
    position: absolute; left: 34px; top: 148px;
    font-family: "Great Vibes", cursive; font-weight: 400;
    font-size: 40px; color: var(--ink-red);
  }
  .contact {
    position: absolute; left: 36px; top: 214px;
    font-family: "Open Sans", sans-serif; color: var(--ink-red);
  }
  .contact .person { font-weight: 600; font-size: 21px; margin-bottom: 14px; }
  .contact .line { font-weight: 400; font-size: 16px; line-height: 22px; }
</style>
</head>
<body>
  <main class="sheet">
    <section class="card card-back" aria-label="Card back">
      <div class="back-mark" aria-hidden="true">Harbouring Dawn Rituals</div>
      <p class="tagline">"Shaping singular, tailored rituals harbouring dawn"</p>
    </section>

    <section class="card card-front" aria-label="Card front">
      <svg class="front-shapes" viewBox="0 0 540 329" preserveAspectRatio="none" aria-hidden="true">
        <path d="M0 118 C 120 150, 250 178, 330 178 C 420 178, 490 170, 540 160 L540 329 L0 329 Z" fill="var(--card-black)"/>
        <path d="M0 106 C 80 120, 170 150, 270 168 C 190 160, 90 140, 0 128 Z" fill="var(--ink-red)"/>
        <path d="M0 100 C 90 112, 180 140, 290 162 C 180 146, 90 122, 0 108 Z" fill="#ffffff" opacity="0.8"/>
      </svg>
      <div class="brand-mark"><span class="dot"></span>Harbouring Dawn Rituals</div>
      <h1 class="business-name">Harbouring Dawn Rituals</h1>
      <div class="contact">
        <p class="person">Doriane Whitcombe</p>
        <p class="line">0428-735902</p>
        <p class="line">harbouringdawnrituals1@examplemail.test</p>
      </div>
    </section>
  </main>
</body>
</html>
```